Stroke Nine Indoor Rowing Center Website

We need a very clean, professional and appealing website for a new company based in Avon, CT (USA) called "Stroke Nine Indoor Rowing Center." Basically, this company as implied by its name is an indoor rowing center that consists of indoor rowing machines (Vantor 7 ergometers, http://www.vantor7.example) and a rowing simulator (called a "glidevator", (http://www.oarmakerlabs.example). These ergometers and simulators will in turn be interfaced with visualization and analysis software (www.pulsewaterly.example) to display "virtual" races and training sessions.

Ultimately, the company will also offer advanced video analysis and 1-1 coaching, but the key message here is to leverage off the company name "Stroke Nine" (which is a term for taking 10 very hard strokes during a rowing race) and the tagline that describes the company ("Indoor Rowing Center").

We have just completed a contest to establish the company's new logo (which I am attaching to this application) and we have some other photos that we think would be helpful in visually describing the company and its services (which I will also attach).

Part of what we like about he logo we selected are the color patterns (which will contrast nicely on both light and dark backgrounds) and the way the concept of a rower is built into the name. In addition, I like the way the number 10 subtly implies IO (as in "input and output" and/or binary numbers to also indicate a "technological dimension" to the company's services).

Also, one of the websites that we really like (that offers a similar progarm and service) in the New York City area is: http://www.harbin-oars.example. The site is clean, informative and easy to navigate. In terms of pages, we'd be looking for the following:

Home
Info (with sub pages for About, Code of Conduct, Experience the Difference, and Careers)
Coaches
Programs*
Blog
Contact
Donate!

*Note that the various programs will be offered and managed through a third-party tool (www.skullhubly.example) and (https://wiki.skullhubly.example/display/FAQ/FAQs#FAQs-WhatfeaturesareavailablethroughyourClubManagementservice%3F) to allow clients to register, sign an electronic waiver and pay for programs and annual memberships. An example of these links is also available at another popular rowing web page, Tidewell Sculling in Boston, MA (https://www.tidewellsculling.example/signup/) or possibly another sign up service called "ZenTrack" (https://www.zentrackhub.example/?ql=softwrfooter)

Finally, we would also like to have links in the navigation bar to connect to social networking sites like Chatterloop, WorkLattice, Quorvo+, etc.

Lastly, I realize that ArtFlock specializes in design only, but we would be interested in receiving estimates for a "turn-key" project that would include coding (or if there are specific partners your design firm works with to codify your designs).

Please let me know if you have any questions or if I can provide any additional information.

Thank you!

Dale

Target Market(s)

Please refer to the attached Powerpoint document for information about target market and the company's vision and mission.

Industry/Entity Type

Electronic

Requirements
Must have
• Clean, intuitive, highly visual and professional look and feel. A color patter and "style guide" that works effectively with the colors and design of our logo that we can build off of as we have new content.

```html
<!DOCTYPE html>
<html lang="en">
<head>
<meta charset="utf-8">
<title>Stroke Nine Indoor Rowing Center</title>
<link href="https://fonts.googleapis.com/css2?family=Signika:wght@400;600&family=Arimo:wght@400;700&family=Ubuntu:wght@400;500&display=swap" rel="stylesheet">
<style>
:root{
  --orange:#f26522;
  --plum:#7a5a6c;
  --text:#333;
  --page-top:#f2f2f2;
  --page-side:#e9e9e9;
  --panel:#fff;
  --footer:#1d1d1d;
  --footer-base:#111;
  --footer-text:#e6e6e6;
  --rule:#3a3a3a;
  --logo-grey:#8c8c8c;
}
*{margin:0;padding:0;box-sizing:border-box}
html,body{width:862px;height:1200px;overflow:hidden}
body{position:relative;background:var(--page-side);font-family:Arimo,Arial,sans-serif;color:var(--text)}
.abs{position:absolute}
.top-band{left:0;top:0;width:862px;height:233px;background:var(--page-top)}
.page{left:46px;top:0;width:770px;height:1010px;background:var(--panel);box-shadow:0 0 8px rgba(0,0,0,.12)}

.utility{top:9px;font-size:9px;color:#555}
.utility-btn{left:710px;top:7px;width:89px;height:15px;background:var(--orange);color:#fff;font-size:9px;line-height:15px;text-align:center;white-space:nowrap}

.brand{left:66px;top:18px}
.brand-name{font-family:Signika,sans-serif;font-weight:600;font-size:42px;line-height:46px;color:var(--orange);letter-spacing:-.3px}
.brand-tag{font-family:Arimo,Arial,sans-serif;font-weight:700;font-size:9.5px;letter-spacing:3.6px;color:#222;margin-top:4px;white-space:nowrap}

.nav{top:66px;height:22px;line-height:22px;font-size:10px;color:#222}
.nav-active{left:392px;width:46px;background:var(--orange);color:#fff;text-align:center}

.hero-frame{left:64px;top:102px;width:734px;height:308px;background:#fff}
.hero{left:67px;top:105px;width:728px;height:304px;background:linear-gradient(90deg,#cfd6cf 0%,#e4e4e2 25%,#f1f1f0 50%,#d9dcd9 75%,#b9c0c0 100%)}
.hero-bar{left:67px;top:368px;width:728px;height:41px;background:rgba(20,20,20,.72)}
.hero-caption{left:74px;top:380px;font-family:Ubuntu,sans-serif;font-weight:500;font-size:13px;color:#fff}

.h-mission{left:74px;top:423px;font-family:Signika,sans-serif;font-weight:600;font-size:17.5px;color:#222}
.h-mission span{color:var(--orange)}
.mission-img{left:74px;top:455px;width:168px;height:122px;background:linear-gradient(135deg,#f4f4f4,#cfd6d4 60%,#f4f4f4)}
.mission-text{left:266px;top:459px;width:526px;font-size:9px;line-height:14.4px;font-family:Ubuntu,sans-serif;color:#333}
.mission-text p+p{margin-top:14px}
.mission-text em{font-weight:500;color:#111}
.divider{left:70px;top:588px;width:726px;height:6px;background:radial-gradient(ellipse at top,rgba(0,0,0,.14),rgba(0,0,0,0) 70%)}

.feature{top:627px;width:158px}
.feature h3{font-family:Signika,sans-serif;font-weight:400;font-size:13px;color:var(--plum);height:25px;padding-left:3px;white-space:nowrap}
.feature p{font-size:8.6px;line-height:11.6px;color:#222;height:53px}
.feature-img{position:relative;width:155px;height:73px;background:linear-gradient(135deg,#8c7a6e,#c9b7a3 55%,#6f6a66)}
.feature-img .more{position:absolute;right:0;bottom:0;background:rgba(0,0,0,.7);color:#fff;font-family:Ubuntu,sans-serif;font-size:9px;padding:1px 5px}

.h-coach{left:84px;top:805px;font-family:Signika,sans-serif;font-weight:600;font-size:17px;color:#111}
.coach-text{left:84px;top:833px;width:696px;font-size:9.6px;line-height:13px;color:#222}
.coach-text p+p{margin-top:13px}

.footer{left:0;top:1001px;width:862px;height:169px;background:var(--footer)}
.footer-base{left:0;top:1170px;width:862px;height:30px;background:var(--footer-base)}

.partners{left:84px;top:969px;width:692px;height:55px;background:#fff;border-radius:10px;box-shadow:0 1px 3px rgba(0,0,0,.3)}
.partner{font-family:Arimo,Arial,sans-serif;font-weight:700;color:#9a9a9a;white-space:nowrap}

.f-head{top:1045px;font-family:Ubuntu,sans-serif;font-weight:400;font-size:15px;color:#fff}
.f-list{top:1071px;list-style:none;font-family:Ubuntu,sans-serif;font-size:9px;line-height:16px;color:var(--footer-text)}
.f-rule{width:1px;top:1066px;height:95px;background:var(--rule)}
.social{top:1048px;width:27px;height:27px}
.f-hr{left:627px;top:1091px;width:147px;height:1px;background:var(--rule)}
.f-brand{left:642px;top:1106px;text-align:center}
.f-brand .brand-name{color:var(--logo-grey);font-size:30px;line-height:32px}
.f-brand .brand-tag{color:#ccc;font-size:7.5px;letter-spacing:2.4px;margin-top:2px}
.base-links{left:77px;top:1174px;font-family:Ubuntu,sans-serif;font-size:8.4px;color:#ccc;line-height:14px}
</style>
</head>
<body>
<div class="abs top-band"></div>
<div class="abs page"></div>

<header>
  <span class="abs utility" style="left:590px">Client Services</span>
  <span class="abs utility" style="left:673px">Login</span>
  <span class="abs utility-btn">More from StrokeNine</span>

  <div class="abs brand">
    <div class="brand-name">Stroke Nine</div>
    <div class="brand-tag">INDOOR ROWING CENTER</div>
  </div>

  <nav>
    <span class="abs nav nav-active">Home</span>
    <span class="abs nav" style="left:458px">Info</span>
    <span class="abs nav" style="left:507px">Coaches</span>
    <span class="abs nav" style="left:575px">Programs</span>
    <span class="abs nav" style="left:648px">Blog</span>
    <span class="abs nav" style="left:699px">Contact</span>
    <span class="abs nav" style="left:764px">Donate!</span>
  </nav>
</header>

<section class="hero-section">
  <div class="abs hero-frame"></div>
  <div class="abs hero" role="img" aria-label="Athletes training on a wooden water rowing machine in a bright home interior"></div>
  <div class="abs hero-bar"></div>
  <div class="abs hero-caption">Find out why our products are used by athletes everywhere</div>
</section>

<section class="mission">
  <h2 class="abs h-mission">Rowing Machines <span>Mission &amp; Goals</span></h2>
  <div class="abs mission-img" role="img" aria-label="Woman exercising on an indoor rowing machine"></div>
  <div class="abs mission-text">
    <p><em><b><i>Stroke Nine Indoor Rowing Center is committed to providing athletic development and personal</i></b></em> growth opportunities for both youth and adults. Ipsum is simply dummy text of the printing and typesetting industry. Lorem Ipsum has been the industry's standard dummy</p>
    <p>Programs introduce new rowers of all ages to the sport, offer training for rowers of all levels of ability (recreational through competitive) and support local youth, collegiate and national team rowing programs.&nbsp; Ipsum is simply dummy text of the print-ing and typesetting industry. Lorem Ipsum has been the industry's standard dummy</p>
  </div>
  <div class="abs divider"></div>
</section>

<section class="features">
  <article class="abs feature" style="left:88px">
    <h3>Founder Profiles</h3>
    <p>Ipsum is simply dummy text of the printing and typesetting industry. Lorem Ipsum has been the industry's standard dummy text...</p>
    <div class="feature-img" role="img" aria-label="Woman rowing on an ergometer in a gym"><span class="more">read more</span></div>
  </article>
  <article class="abs feature" style="left:264px">
    <h3>Floor plan &amp; Equipment</h3>
    <p>Ipsum is simply dummy text of the printing and typesetting industry. Lorem Ipsum has been the industry's standard dummy text...</p>
    <div class="feature-img" role="img" aria-label="Rowing machine in a wood-panelled room"><span class="more">read more</span></div>
  </article>
  <article class="abs feature" style="left:444px">
    <h3>Key Differentiators</h3>
    <p>Ipsum is simply dummy text of the printing and typesetting industry. Lorem Ipsum has been the industry's standard dummy text...</p>
    <div class="feature-img" role="img" aria-label="Rower pulling the handle in a fitness studio"><span class="more">read more</span></div>
  </article>
  <article class="abs feature" style="left:624px">
    <h3>Marketing</h3>
    <p>Ipsum is simply dummy text of the printing and typesetting industry. Lorem Ipsum has been the industry's standard dummy text...</p>
    <div class="feature-img" role="img" aria-label="Woman rowing in a brick-walled loft"><span class="more">read more</span></div>
  </article>
</section>

<section class="coaching">
  <h2 class="abs h-coach">Best coaching platform in the world</h2>
  <div class="abs coach-text">
    <p>Ipsum is simply dummy text of the printing and typesetting industry. Lorem Ipsum has been the industry's standard dummy text ever since the 1500s, when an unknown printer took a galley of type and scrambled it to make a type specimen book. It has survived not only five centuries, but also the leap into electronic typesetting, remaining essentially unchanged. It was popularised in the 1960s with the release of Letterkit sheets containing Lorem Ipsum passages, and more recently with desktop publishing software like Pagecraft Studio including versions of Lorem Ipsum.</p>
    <p>Ipsum is simply dummy text of the printing and typesetting industry. Lorem Ipsum has been the industry's standard dummy text ever since the 1500s, when an unknown printer took a galley of type and scrambled it to make a type specimen book. It has survived not only five centuries, but also the leap into electronic typesetting, remaining essentially unchanged. It was popularised in the 1960s with the release....</p>
  </div>
</section>

<footer>
  <div class="abs footer"></div>
  <div class="abs footer-base"></div>

  <div class="abs partners"></div>
  <svg class="abs" style="left:93px;top:986px" width="14" height="22" viewBox="0 0 14 22"><path d="M11 2 L3 11 L11 20" fill="none" stroke="#222" stroke-width="3"/></svg>
  <svg class="abs" style="left:755px;top:986px" width="14" height="22" viewBox="0 0 14 22"><path d="M3 2 L11 11 L3 20" fill="none" stroke="#222" stroke-width="3"/></svg>
  <span class="abs partner" style="left:130px;top:980px;font-size:18px">GlideRow</span>
  <span class="abs partner" style="left:200px;top:1001px;font-size:10px">AquaStroke</span>
  <span class="abs partner" style="left:305px;top:995px;font-size:9px">TideCoach</span>
  <span class="abs partner" style="left:392px;top:983px;font-size:20px">PaddleTek</span>
  <span class="abs partner" style="left:535px;top:978px;font-size:30px">Surgeline</span>

  <h4 class="abs f-head" style="left:103px">Quick Links</h4>
  <ul class="abs f-list" style="left:105px">
    <li>Lorem ipsum dolor sit</li><li>Amet consectetuer</li><li>Adipiscing elit</li><li>Praesent vestibulum</li><li>Molestie lacus aenean</li>
  </ul>
  <div class="abs f-rule" style="left:249px"></div>

  <h4 class="abs f-head" style="left:292px">How it Works</h4>
  <ul class="abs f-list" style="left:295px;top:1072px">
    <li>Lorem ipsum dolor sit</li><li>Amet consectetuer</li><li>Adipiscing elit</li><li>Praesent vestibulum</li><li>Molestie lacus aenean</li>
  </ul>
  <div class="abs f-rule" style="left:431px"></div>

  <h4 class="abs f-head" style="left:458px;top:1047px">Contact Us</h4>
  <ul class="abs f-list" style="left:460px;top:1072px">
    <li>34 StrokeNineIndoor</li><li>Millbrook, MB4 2QT</li><li>Phone:+44(0)1632 960418</li><li>Email:info@strokenine.example</li>
  </ul>

  <div class="abs social" style="left:648px;background:#f26522" aria-label="Feed"></div>
  <div class="abs social" style="left:679px;background:#3b5998" aria-label="Chatterloop"></div>
  <div class="abs social" style="left:710px;background:#d0402d" aria-label="Quorvo+"></div>
  <div class="abs social" style="left:746px;background:#2fa8e0" aria-label="Chirpwell"></div>
  <div class="abs f-hr"></div>

  <div class="abs f-brand">
    <div class="brand-name">Stroke Nine</div>
    <div class="brand-tag">INDOOR ROWING CENTER</div>
  </div>

  <div class="abs base-links">
    Home &nbsp;|&nbsp; Info &nbsp;|&nbsp; Coaches &nbsp;|&nbsp; Programs &nbsp;|&nbsp; Blog &nbsp;|&nbsp; Contact &nbsp;|&nbsp; Donate!<br>
    © 2013 Stroke Nine Indoor Rowing Center. &nbsp; FAQ &nbsp;|&nbsp; Privacy Policy &nbsp;|&nbsp; Site Map.
  </div>
</footer>
</body>
</html>
```